Mosquito Repellent Wet Wipes pacakage design

We are a mosquito repellent manufacturer under the brand name "Zest Guard". We have a product currently and are looking to make it more attractive.

Our product is a mosquito repellent wipe that can be applied on skin and clothing for protection against mosquitoes. It is going to be available in sachets. Customer age groups include ages 10-30 as well as Moms who are key decision makers.

We are looking for a friendly package in terms of color and appeal and a redesign of Zest Guard logo. I am attaching our current product pictures and brochure. Hope this gets you started. We are attaching information on the spray bottle.

Visit www.tolvanhealthworks.com for more details.

Package Dimension Folded : 80x60 mm
Package Dimension unfolded: 80 x 120 mm

Thank you
Varun
Updates

Project Deadline Extended Reason: Still not happy with the designs that are submitted. Like to see more designs. Added Thursday, February 18, 2016

Target Market(s)

General population with more focus on age groups 10-30 as well as Moms

Industry/Entity Type

Cosmetics

Requirements
Must have
• Statutory information should be provided on the product including Manufacturing address, ingredient name & bar code. I guess we can do this once the package is finalized

```html
<!DOCTYPE html>
<html lang="en">
<head>
<meta charset="utf-8">
<title>Zest Guard Insect Repellent Wipes – Sachet Design</title>
<link rel="stylesheet" href="https://fonts.googleapis.com/css2?family=Barlow+Condensed:ital,wght@0,300;0,400;0,600;0,700;1,400;1,700&display=swap">
<style>
  :root {
    --blue: #00a8e8;
    --green: #8cc63f;
    --ink: #2b2b2b;
    --foil: #ffffff;
    --foil-edge: #d9d9d9;
    --crimp-line: #cfcfcf;
    --stage-light: #fbfbfb;
    --stage-dark: #e4e4e4;
  }
  html, body {
    margin: 0;
    padding: 0;
    width: 1200px;
    height: 1200px;
    overflow: hidden;
  }
  body {
    background: radial-gradient(ellipse at 50% 35%, var(--stage-light) 0%, var(--stage-dark) 100%);
    font-family: "Barlow Condensed", "Arial Narrow", sans-serif;
    position: relative;
  }

  /* ---------- Standalone brand name ---------- */
  .brand-mark {
    position: absolute;
    left: 108px;
    top: 96px;
    margin: 0;
    font-size: 112px;
    font-weight: 700;
    line-height: 1;
    color: var(--blue);
    letter-spacing: -1px;
  }

  /* ---------- Shared sachet shell ---------- */
  .sachet {
    position: absolute;
  }
  .sachet-shell {
    position: absolute;
    inset: 0;
    overflow: visible;
  }
  .maker-name {
    font-weight: 700;
    color: var(--green);
    display: flex;
    align-items: center;
    gap: 8px;
    line-height: 1;
  }
  .maker-name .maker-dot {
    width: 0.7em;
    height: 0.7em;
    border-radius: 50%;
    background: var(--blue);
  }

  /* ---------- Front face ---------- */
  .sachet-front {
    left: 100px;
    top: 330px;
    width: 440px;
    height: 595px;
  }
  .sachet-front .maker-name {
    position: absolute;
    left: 54px;
    top: 80px;
    font-size: 30px;
  }
  .front-brand {
    position: absolute;
    left: 0;
    right: 0;
    top: 150px;
    margin: 0;
    text-align: center;
    font-size: 80px;
    font-weight: 700;
    line-height: 1;
    color: var(--blue);
    letter-spacing: -1px;
  }
  .product-band {
    position: absolute;
    left: 42px;
    width: 354px;
    top: 250px;
    height: 50px;
    background: var(--green);
    color: #fff;
    font-weight: 700;
    font-size: 38px;
    line-height: 50px;
    text-align: center;
    letter-spacing: 0.3px;
  }
  .claim-panel {
    position: absolute;
    left: 42px;
    top: 300px;
    width: 354px;
    height: 136px;
  }
  .claim-panel svg {
    position: absolute;
    inset: 0;
  }
  .claim-text {
    position: relative;
    margin: 0;
    padding-top: 8px;
    text-align: center;
    color: #fff;
    line-height: 1.15;
  }
  .claim-text .claim-lead {
    display: block;
    font-weight: 300;
    font-size: 24px;
  }
  .claim-text .claim-diseases {
    display: block;
    font-weight: 700;
    font-size: 24px;
  }
  .lasting-badge {
    position: absolute;
    right: 44px;
    top: 404px;
    width: 150px;
    text-align: center;
    color: var(--green);
    line-height: 1;
  }
  .lasting-badge .lasting-top {
    display: block;
    font-weight: 700;
    font-size: 22px;
  }
  .lasting-badge .lasting-art {
    display: block;
    width: 40px;
    height: 22px;
    margin: 3px auto 3px;
    background: linear-gradient(180deg, #7fd0f0, var(--blue));
    border-radius: 4px;
    opacity: 0.55;
  }
  .lasting-badge .lasting-main {
    display: block;
    font-weight: 700;
    font-size: 28px;
  }
  .fresh-note {
    position: absolute;
    left: 52px;
    top: 474px;
    margin: 0;
    color: var(--blue);
    font-weight: 700;
    font-size: 21px;
    line-height: 1.2;
    text-align: center;
  }
  .pack-size {
    position: absolute;
    right: 50px;
    top: 500px;
    margin: 0;
    color: var(--blue);
    font-weight: 700;
    font-size: 17px;
  }
  .pack-size .divider {
    display: inline-block;
    width: 1px;
    height: 16px;
    background: var(--blue);
    margin: 0 5px;
    vertical-align: -3px;
  }

  /* ---------- Back face ---------- */
  .sachet-back {
    left: 580px;
    top: 480px;
    width: 520px;
    height: 310px;
  }
  .back-intro {
    position: absolute;
    left: 62px;
    top: 22px;
    width: 396px;
    margin: 0;
    font-size: 14px;
    line-height: 1.22;
    color: var(--ink);
  }
  .back-intro strong {
    font-weight: 700;
    font-style: italic;
  }
  .back-brand {
    position: absolute;
    left: 62px;
    top: 98px;
    margin: 0;
    font-size: 40px;
    font-weight: 700;
    line-height: 1;
    color: var(--blue);
  }
  .usage-info {
    position: absolute;
    left: 62px;
    top: 180px;
    width: 250px;
    margin: 0;
    font-size: 13.5px;
    line-height: 1.3;
    color: var(--ink);
  }
  .usage-info b {
    font-weight: 700;
  }
  .back-maker {
    position: absolute;
    right: 62px;
    top: 180px;
    text-align: right;
  }
  .back-maker .maker-name {
    font-size: 26px;
    justify-content: flex-end;
  }
  .back-maker .maker-web {
    display: block;
    margin-top: 4px;
    font-size: 13px;
    color: var(--ink);
  }
  .back-lasting {
    position: absolute;
    right: 62px;
    top: 244px;
    text-align: right;
    color: var(--green);
    font-weight: 700;
    line-height: 1;
  }
  .back-lasting .lasting-top {
    display: block;
    font-size: 14px;
  }
  .back-lasting .lasting-main {
    display: block;
    font-size: 20px;
  }
</style>
</head>
<body>

  <h1 class="brand-mark">Zest Guard</h1>

  <!-- Front face of the sachet -->
  <section class="sachet sachet-front" aria-label="Sachet front">
    <svg class="sachet-shell" viewBox="0 0 440 595" width="440" height="595" aria-hidden="true">
      <defs>
        <linearGradient id="foilFront" x1="0" y1="0" x2="1" y2="0">
          <stop offset="0" stop-color="#e3e3e3"/>
          <stop offset="0.08" stop-color="#ffffff"/>
          <stop offset="0.92" stop-color="#ffffff"/>
          <stop offset="1" stop-color="#dcdcdc"/>
        </linearGradient>
      </defs>
      <path fill="url(#foilFront)" stroke="var(--foil-edge)" stroke-width="1"
        d="M0,14 L11,4 L22,14 L33,4 L44,14 L55,4 L66,14 L77,4 L88,14 L99,4 L110,14 L121,4 L132,14 L143,4 L154,14 L165,4 L176,14 L187,4 L198,14 L209,4 L220,14 L231,4 L242,14 L253,4 L264,14 L275,4 L286,14 L297,4 L308,14 L319,4 L330,14 L341,4 L352,14 L363,4 L374,14 L385,4 L396,14 L407,4 L418,14 L429,4 L440,14
           L440,581 L429,591 L418,581 L407,591 L396,581 L385,591 L374,581 L363,591 L352,581 L341,591 L330,581 L319,591 L308,581 L297,591 L286,581 L275,591 L264,581 L253,591 L242,581 L231,591 L220,581 L209,591 L198,581 L187,591 L176,581 L165,591 L154,581 L143,591 L132,581 L121,591 L110,581 L99,591 L88,581 L77,591 L66,581 L55,591 L44,581 L33,591 L22,581 L11,591 L0,581 Z"/>
      <g stroke="var(--crimp-line)" stroke-width="1.5">
        <line x1="0" y1="28" x2="440" y2="28"/>
        <line x1="0" y1="36" x2="440" y2="36"/>
        <line x1="0" y1="44" x2="440" y2="44"/>
        <line x1="0" y1="52" x2="440" y2="52"/>
        <line x1="0" y1="540" x2="440" y2="540"/>
        <line x1="0" y1="548" x2="440" y2="548"/>
        <line x1="0" y1="556" x2="440" y2="556"/>
        <line x1="0" y1="564" x2="440" y2="564"/>
      </g>
    </svg>

    <div class="maker-name"><span class="maker-dot"></span>Tolvan</div>

    <h2 class="front-brand">Zest Guard</h2>

    <div class="product-band">INSECT REPELLENT WIPES</div>

    <div class="claim-panel">
      <svg viewBox="0 0 354 136" width="354" height="136" aria-hidden="true">
        <path fill="var(--blue)" d="M0,0 H354 V84 H150 Q176,100 178,136 H18 Q0,136 0,118 Z"/>
        <path fill="#ffffff" d="M150,84 H354 L178,136 Q176,100 150,84 Z"/>
        <path fill="none" stroke="var(--blue)" stroke-width="2" d="M150,84 Q176,100 178,136"/>
      </svg>
      <p class="claim-text">
        <span class="claim-lead">Repels Mosquitoes that may carry</span>
        <span class="claim-diseases">MALARIA, CHIKUNGUNYA &amp; DENGUE</span>
      </p>
    </div>

    <div class="lasting-badge">
      <span class="lasting-top">Long Lasting</span>
      <span class="lasting-art" role="img" aria-label="Small mosquito illustration"></span>
      <span class="lasting-main">PROTECTION</span>
    </div>

    <p class="fresh-note">Light &amp; Fresh with<br>OLIVE EXTRACTS</p>

    <p class="pack-size">1Wipe<span class="divider"></span>12cmx15cm</p>
  </section>

  <!-- Back face of the sachet -->
  <section class="sachet sachet-back" aria-label="Sachet back">
    <svg class="sachet-shell" viewBox="0 0 520 310" width="520" height="310" aria-hidden="true">
      <defs>
        <linearGradient id="foilBack" x1="0" y1="0" x2="0" y2="1">
          <stop offset="0" stop-color="#e6e6e6"/>
          <stop offset="0.1" stop-color="#ffffff"/>
          <stop offset="0.9" stop-color="#ffffff"/>
          <stop offset="1" stop-color="#dddddd"/>
        </linearGradient>
      </defs>
      <path fill="url(#foilBack)" stroke="var(--foil-edge)" stroke-width="1"
        d="M14,0 L506,0 L516,12 L506,25 L516,38 L506,51 L516,64 L506,77 L516,90 L506,103 L516,116 L506,129 L516,142 L506,155 L516,168 L506,181 L516,194 L506,207 L516,220 L506,233 L516,246 L506,259 L516,272 L506,285 L516,298 L506,310
           L14,310 L4,298 L14,285 L4,272 L14,259 L4,246 L14,233 L4,220 L14,207 L4,194 L14,181 L4,168 L14,155 L4,142 L14,129 L4,116 L14,103 L4,90 L14,77 L4,64 L14,51 L4,38 L14,25 L4,12 Z"/>
      <g stroke="var(--crimp-line)" stroke-width="1.5">
        <line x1="26" y1="0" x2="26" y2="310"/>
        <line x1="33" y1="0" x2="33" y2="310"/>
        <line x1="40" y1="0" x2="40" y2="310"/>
        <line x1="47" y1="0" x2="47" y2="310"/>
        <line x1="473" y1="0" x2="473" y2="310"/>
        <line x1="480" y1="0" x2="480" y2="310"/>
        <line x1="487" y1="0" x2="487" y2="310"/>
        <line x1="494" y1="0" x2="494" y2="310"/>
      </g>
      <rect x="0" y="148" width="520" height="20" fill="#f4f4f4"/>
      <g stroke="var(--crimp-line)" stroke-width="1.2">
        <line x1="0" y1="148" x2="520" y2="148"/>
        <line x1="0" y1="153" x2="520" y2="153"/>
        <line x1="0" y1="158" x2="520" y2="158"/>
        <line x1="0" y1="163" x2="520" y2="163"/>
        <line x1="0" y1="168" x2="520" y2="168"/>
      </g>
    </svg>

    <p class="back-intro"><strong>Our product is a mosquito repellent wipe</strong> that can be applied on skin and clothing for protection against mosquitoes. It is going to be available in sachets. Customer age groups include ages 10-30 as well as Moms who are key decision makers.</p>

    <h2 class="back-brand">Zest Guard</h2>

    <p class="usage-info">
      <b>Usage instruction:</b> that can be applied on skin and clothing for protection against mosquitoes.<br>
      <b>Ingredients:</b> DEET 15% ; OTHERS 85%<br>
      <b>Manufactured by:</b> Tolvan.
    </p>

    <div class="back-maker">
      <div class="maker-name"><span class="maker-dot"></span>Tolvan</div>
      <span class="maker-web">www.tolvanhealthworks.com</span>
    </div>

    <div class="back-lasting">
      <span class="lasting-top">Long Lasting</span>
      <span class="lasting-main">PROTECTION</span>
    </div>
  </section>

</body>
</html>
```